Psychotherapist need a business card with logo

I am a psychotherapist in need of a business card. The card must have:

Marisol Trevuneda
Psicoterapeuta
937 281 706

Psychologists use the greek letter psy, which is the psychologist symbol, but I would prefer something like a mandala, a graphic symbol, an iconic tree, nothing very usual, but something that shows confidence and trust.

Industry/Entity Type

Business

```html
<!DOCTYPE html>
<html lang="es">
<head>
<meta charset="utf-8">
<title>Marisol Trevuneda – Tarjetas de visita</title>
<link href="https://fonts.googleapis.com/css2?family=Great+Vibes&family=Questrial&display=swap" rel="stylesheet">
<style>
  :root {
    --paper: #ffffff;
    --card-beige: #e3d7c3;
    --card-beige-light: #e6dcc8;
    --brown: #3f2b2b;
    --cream-line: #f3ece0;
    --mandala-fill: #e9dfcd;
  }
  html, body {
    margin: 0;
    padding: 0;
    overflow: hidden;
    background: var(--paper);
  }
  .sheet {
    position: relative;
    width: 1200px;
    height: 900px;
    background: var(--paper);
  }
  .card {
    position: absolute;
    width: 481px;
    height: 265px;
    border-radius: 5px;
    overflow: hidden;
    background: var(--card-beige);
  }
  .card svg.card-art {
    position: absolute;
    inset: 0;
    width: 481px;
    height: 265px;
  }
  .card-text {
    position: absolute;
    left: 0;
    right: 0;
    text-align: center;
    color: var(--brown);
  }
  .holder-name {
    font-family: "Great Vibes", cursive;
    font-size: 42px;
    line-height: 1;
    margin: 0;
    font-weight: 400;
  }
  .holder-role,
  .holder-phone {
    font-family: "Questrial", sans-serif;
    font-size: 16px;
    line-height: 1;
    margin: 0;
  }
  .holder-role { margin-top: 10px; }
  .holder-phone { margin-top: 10px; font-size: 17px; }

  .card--lines    { left: 91px;  top: 38px; }
  .card--waves    { left: 614px; top: 38px; }
  .card--pillars  { left: 91px;  top: 320px; }
  .card--arcs     { left: 614px; top: 320px; }
  .card--tabs     { left: 91px;  top: 603px; }
  .card--panels   { left: 614px; top: 603px; background: var(--brown); }
</style>
</head>
<body>
<main class="sheet">

  <!-- Card: straight bands -->
  <section class="card card--lines">
    <svg class="card-art" viewBox="0 0 481 265">
      <rect x="0" y="0" width="481" height="10" fill="var(--brown)"/>
      <rect x="0" y="15" width="481" height="3" fill="var(--brown)"/>
      <rect x="0" y="252" width="481" height="13" fill="var(--brown)"/>
      <g role="img" aria-label="Mandala emblem">
        <circle cx="244" cy="137" r="101" fill="var(--mandala-fill)" stroke="var(--cream-line)" stroke-width="4"/>
      </g>
    </svg>
    <div class="card-text" style="top:100px">
      <p class="holder-name">Marisol Trevuneda</p>
      <p class="holder-role">Psicoterapeuta</p>
      <p class="holder-phone">937 281 706</p>
    </div>
  </section>

  <!-- Card: flowing waves -->
  <section class="card card--waves">
    <svg class="card-art" viewBox="0 0 481 265">
      <path d="M0 0 H481 V58 C420 45 350 0 250 12 C170 22 90 12 0 8 Z" fill="var(--brown)"/>
      <path d="M0 14 C90 18 170 28 250 18 C350 6 420 50 481 64" fill="none" stroke="var(--brown)" stroke-width="1.5"/>
      <path d="M0 265 V240 C60 215 140 205 250 230 C340 250 420 250 481 243 V265 Z" fill="var(--brown)"/>
      <path d="M0 234 C60 209 140 199 250 224 C340 244 420 244 481 237" fill="none" stroke="var(--brown)" stroke-width="1.5"/>
      <g role="img" aria-label="Mandala emblem">
        <circle cx="238" cy="126" r="88" fill="var(--mandala-fill)" stroke="var(--cream-line)" stroke-width="4"/>
      </g>
    </svg>
    <div class="card-text" style="top:96px">
      <p class="holder-name" style="font-size:38px">Marisol Trevuneda</p>
      <p class="holder-role" style="margin-top:8px;font-size:15px">Psicoterapeuta</p>
      <p class="holder-phone" style="margin-top:6px;font-size:16px">937 281 706</p>
    </div>
  </section>

  <!-- Card: vertical pillars -->
  <section class="card card--pillars">
    <svg class="card-art" viewBox="0 0 481 265">
      <rect x="0" y="0" width="21" height="265" fill="var(--brown)"/>
      <rect x="28" y="0" width="4" height="265" fill="var(--brown)"/>
      <rect x="44" y="0" width="5" height="265" fill="var(--brown)"/>
      <rect x="431" y="0" width="5" height="265" fill="var(--brown)"/>
      <rect x="444" y="0" width="5" height="265" fill="var(--brown)"/>
      <rect x="459" y="0" width="22" height="265" fill="var(--brown)"/>
      <g role="img" aria-label="Mandala emblem">
        <circle cx="239" cy="133" r="101" fill="var(--mandala-fill)" stroke="var(--cream-line)" stroke-width="4"/>
      </g>
    </svg>
    <div class="card-text" style="top:96px">
      <p class="holder-name">Marisol Trevuneda</p>
      <p class="holder-role">Psicoterapeuta</p>
      <p class="holder-phone">937 281 706</p>
    </div>
  </section>

  <!-- Card: gentle arcs -->
  <section class="card card--arcs">
    <svg class="card-art" viewBox="0 0 481 265">
      <path d="M0 0 H481 V20 C320 10 160 10 0 18 Z" fill="var(--brown)"/>
      <path d="M0 24 C160 16 320 16 481 26" fill="none" stroke="var(--brown)" stroke-width="1.5"/>
      <path d="M0 265 V252 C160 242 320 240 481 248 V265 Z" fill="var(--brown)"/>
      <path d="M0 246 C160 236 320 234 481 242" fill="none" stroke="var(--brown)" stroke-width="1.5"/>
      <g role="img" aria-label="Mandala emblem">
        <circle cx="237" cy="131" r="101" fill="var(--mandala-fill)" stroke="var(--cream-line)" stroke-width="4"/>
      </g>
    </svg>
    <div class="card-text" style="top:96px">
      <p class="holder-name">Marisol Trevuneda</p>
      <p class="holder-role">Psicoterapeuta</p>
      <p class="holder-phone">937 281 706</p>
    </div>
  </section>

  <!-- Card: side tabs -->
  <section class="card card--tabs">
    <svg class="card-art" viewBox="0 0 481 265">
      <rect x="0" y="0" width="481" height="14" fill="var(--brown)"/>
      <rect x="0" y="252" width="481" height="13" fill="var(--brown)"/>
      <path d="M0 81 H32 Q41 81 41 92 V143 Q41 154 32 154 H0 Z" fill="var(--brown)"/>
      <path d="M481 81 H449 Q440 81 440 92 V143 Q440 154 449 154 H481 Z" fill="var(--brown)"/>
      <g role="img" aria-label="Mandala emblem">
        <circle cx="244" cy="131" r="101" fill="var(--mandala-fill)" stroke="var(--cream-line)" stroke-width="4"/>
      </g>
    </svg>
    <div class="card-text" style="top:94px">
      <p class="holder-name">Marisol Trevuneda</p>
      <p class="holder-role">Psicoterapeuta</p>
      <p class="holder-phone">937 281 706</p>
    </div>
  </section>

  <!-- Card: dark side panels -->
  <section class="card card--panels">
    <svg class="card-art" viewBox="0 0 481 265">
      <rect x="0" y="0" width="76" height="265" fill="var(--brown)" role="img" aria-label="Dark floral pattern panel"/>
      <rect x="406" y="0" width="75" height="265" fill="var(--brown)" role="img" aria-label="Dark floral pattern panel"/>
      <rect x="76" y="0" width="330" height="265" rx="5" fill="var(--card-beige-light)"/>
      <g role="img" aria-label="Mandala emblem">
        <circle cx="238" cy="132" r="101" fill="var(--mandala-fill)" stroke="var(--cream-line)" stroke-width="4"/>
      </g>
    </svg>
    <div class="card-text" style="top:96px">
      <p class="holder-name">Marisol Trevuneda</p>
      <p class="holder-role">Psicoterapeuta</p>
      <p class="holder-phone">937 281 706</p>
    </div>
  </section>

</main>
</body>
</html>
```